Brindlow Telescoping Flagpole Brochure

I believe our current brochure is too busy. I would like to but it on smaller paper, make it less busy and focus on the fact that we have metal hooks in our locking system.

Target Market(s)

People you attend fairs, home and garden shows. Usually ages 40+ . A lot of people who served in the military.

Requirements
Must have
• Our Metal Hook locking system makes us stand out from everyone else. Made in the USA on the brochure.

```html
<!DOCTYPE html>
<html lang="en">
<head>
<meta charset="utf-8">
<title>Brindlow Telescoping Flagpole Brochure</title>
<link rel="stylesheet" href="https://fonts.googleapis.com/css2?family=Oswald:wght@600&family=Baloo+2:wght@500;600;700&family=Exo:ital,wght@0,400;0,600;1,400&display=swap">
<style>
:root{
  --red:#b11f26;
  --navy:#2e3192;
  --ink:#2b2b2b;
  --text:#333333;
  --white:#ffffff;
  --lawn:#5f8a3c;
  --sky:#9fb8d8;
  --tile:#c9262c;
  --rule:#a82328;
}
*{margin:0;padding:0;box-sizing:border-box}
html,body{width:928px;height:1200px;overflow:hidden;background:var(--white)}
.brochure{position:relative;width:928px;height:1200px;border:1px solid #bdbdbd;font-family:"Exo",sans-serif;color:var(--text)}
.photo{position:absolute}
.hero-photo-a{left:0;top:0;width:235px;height:173px;background:linear-gradient(#dfe6ee 0%,#e9e6df 45%,var(--lawn) 62%,#4f7a30 100%)}
.hero-photo-b{left:237px;top:0;width:129px;height:173px;background:linear-gradient(#2f62b8 0%,var(--sky) 45%,#cfd3d6 55%,var(--lawn) 70%,#4a7530 100%)}
.headline{position:absolute;left:366px;top:0;width:562px;height:173px;background:var(--red);display:flex;align-items:center;justify-content:center;text-align:center}
.headline h1{font-family:"Oswald",sans-serif;font-weight:600;color:var(--white);font-size:27px;line-height:34px;letter-spacing:1.6px;text-transform:uppercase}
.feature-photo{position:absolute;left:27px;top:192px;width:454px;height:308px;border:4px solid var(--navy);background:linear-gradient(90deg,#3a3a3a 0%,#6a7a6a 18%,#f1f1f1 40%,#e9d24a 62%,#c7c9cc 80%,#8a8f95 100%)}
.tab{position:absolute;height:38px;display:flex;align-items:center;justify-content:center}
.tab svg{position:absolute;inset:0;width:100%;height:100%}
.tab span{position:relative;font-family:"Baloo 2",sans-serif;font-weight:600;color:var(--white);font-size:25px;line-height:1;padding-top:3px}
.tab-why{left:506px;top:195px;width:394px}
.tab-accessories{left:309px;top:540px;width:309px}
.intro{position:absolute;left:507px;top:258px;width:394px;font-size:16.6px;line-height:20.6px;text-align:justify;color:var(--text)}
.intro p+p{margin-top:18px}
.intro strong{font-weight:600;color:var(--red)}
.callout{position:absolute;left:507px;top:442px;width:394px;height:58px;border-left:6px solid var(--red);background:#f4f4f8;display:flex;flex-direction:column;justify-content:center;padding-left:14px}
.callout .feature{font-family:"Baloo 2",sans-serif;font-weight:700;font-size:20px;line-height:22px;color:var(--red)}
.callout .origin{font-family:"Baloo 2",sans-serif;font-weight:600;font-size:17px;line-height:20px;color:var(--navy);letter-spacing:.5px}
.accessory{position:absolute;width:94px;text-align:center}
.accessory .thumb{width:94px;height:94px;border:3px solid var(--navy);border-radius:5px;background:linear-gradient(160deg,#d63a3f,var(--tile) 60%,#9e1c22)}
.accessory .label{position:absolute;top:103px;left:-30px;width:154px;font-size:13.6px;color:var(--ink)}
.sizes{position:absolute;left:55px;top:931px;width:818px;height:62px;border-radius:12px;background:var(--navy);color:var(--white);text-align:center;padding-top:7px}
.sizes h2{font-family:"Baloo 2",sans-serif;font-weight:600;font-size:20px;line-height:22px}
.sizes p{font-size:17px;line-height:23px}
.sizes small{font-size:13.6px}
.sizes .sep{margin:0 9px}
.specs{position:absolute;left:60px;top:1014px;width:808px;text-align:center;font-style:italic;font-size:14px;line-height:19px;color:var(--text)}
.divider{position:absolute;left:28px;top:1080px;width:872px;height:12px}
.mailing{position:absolute;left:0;top:1114px;width:928px;text-align:center;font-size:34px;color:var(--ink)}
</style>
</head>
<body>
<main class="brochure">
  <div class="photo hero-photo-a" role="img" aria-label="Photo of a house front yard with a flagpole in a red mulch bed"></div>
  <div class="photo hero-photo-b" role="img" aria-label="Photo of a tall flagpole flying the American flag on a lawn"></div>
  <header class="headline">
    <h1>The best way to display your<br>pride is by flying your colors on the<br>Brindlow telescoping flagpole</h1>
  </header>

  <div class="photo feature-photo" role="img" aria-label="Photo of three telescoping flagpoles in black, white and silver showing the metal hook locking sleeves"></div>

  <div class="tab tab-why">
    <svg viewBox="0 0 394 38" preserveAspectRatio="none" aria-hidden="true"><polygon points="14,0 394,0 380,38 0,38" fill="#b11f26"/></svg>
    <span>Why the Brindlow Flagpole ?</span>
  </div>
  <section class="intro">
    <p>The latest in flagpole technology makes it simple for homeowners and businesses to display their colors. The Brindlow Flagpole pioneered the telescopic flagpole industry.</p>
    <p>Our <strong>metal hook locking system</strong> makes us stand out from everyone else. Strong metal hooks lock each section in place, no pins, no rings.</p>
  </section>
  <div class="callout">
    <span class="feature">Metal Hook Locking System</span>
    <span class="origin">Proudly Made in the USA</span>
  </div>

  <div class="tab tab-accessories">
    <svg viewBox="0 0 309 38" preserveAspectRatio="none" aria-hidden="true"><polygon points="14,0 309,0 295,38 0,38" fill="#b11f26"/></svg>
    <span>Accessories</span>
  </div>

  <div class="accessory" style="left:153px;top:618px"><div class="thumb" role="img" aria-label="Photo of swivel ring"></div><div class="label">Swivel Ring</div></div>
  <div class="accessory" style="left:285px;top:618px"><div class="thumb" role="img" aria-label="Photo of ground sleeve"></div><div class="label">Ground Sleeve</div></div>
  <div class="accessory" style="left:417px;top:618px"><div class="thumb" role="img" aria-label="Photo of base collar"></div><div class="label">Base Collar</div></div>
  <div class="accessory" style="left:549px;top:618px"><div class="thumb" role="img" aria-label="Photo of hitch mount"></div><div class="label">Hitch Mount</div></div>
  <div class="accessory" style="left:681px;top:618px"><div class="thumb" role="img" aria-label="Photo of wall mount"></div><div class="label">Wall Mount</div></div>
  <div class="accessory" style="left:219px;top:764px"><div class="thumb" role="img" aria-label="Photo of locking clamp"></div><div class="label">Locking Clamp</div></div>
  <div class="accessory" style="left:351px;top:764px"><div class="thumb" role="img" aria-label="Photo of wheel stand"></div><div class="label">Wheel Stand</div></div>
  <div class="accessory" style="left:483px;top:764px"><div class="thumb" role="img" aria-label="Photo of dock mount"></div><div class="label">Dock Mount</div></div>
  <div class="accessory" style="left:615px;top:764px"><div class="thumb" role="img" aria-label="Photo of light kit"></div><div class="label">Light Kit</div></div>

  <section class="sizes">
    <h2>Available Pole Sizes :</h2>
    <p>16ft. pole <small>(2.5in. base diameter)</small><span class="sep">•</span>22ft. pole <small>(3in. base diameter)</small><span class="sep">•</span>25ft. pole <small>(3in. base diameter)</small></p>
  </section>

  <p class="specs">High strength 6000 series T6 aluminum with a larger base tube, 30% stronger than the competitor's poles,<br>finished in an architectural hard anodized coat. Made in the USA.</p>

  <svg class="divider" viewBox="0 0 872 12" aria-hidden="true">
    <line x1="0" y1="6" x2="872" y2="6" stroke="#a82328" stroke-width="2"/>
    <circle cx="436" cy="6" r="5" fill="#a82328"/>
  </svg>

  <p class="mailing">Space for Mailing Address</p>
</main>
</body>
</html>
```